New Business Card for Web Design/Internet Marketing Company

Looking for a great looking new business card. We are a 10 year old web design, internet marketing and website management company that works mostly with small businesses.

Our new card needs to better match the colors and style of our website, be bold, extremely usable and slightly edgy.

Target Market(s)

Small/Medium businesses that have websites

Industry/Entity Type

Internet

Requirements
Must have
• Front and back design, full color, rounded corners please

Must use the colors/style of our website (JPG provided)

INFO FOR CARDS (as readable as possible please)
Mark Pellow
President/CEO
mark@brightlanesites.com
Phone: 520-481-7093
Toll Free: 866-481-7093
Address: 4315 E. Kestrel Ave. Ste. 140, Tucson, AZ 85733

THINGS I WANT TO PROMOTE (if there is room):
1. Our Website - www.brightlanesites.com

2. Social Media
Twitter: @brightlanesites
Facebook: www.facebook.com/brightlanesites

3. Our Services
Web Design
Internet Marketing
Website Management

```html
<!DOCTYPE html>
<html lang="en">
<head>
<meta charset="utf-8">
<title>Bright Lane Sites – Business Card Back</title>
<link href="https://fonts.googleapis.com/css2?family=Source+Sans+3:wght@400&display=swap" rel="stylesheet">
<style>
  :root {
    --page-bg: #dcedf7;
    --card-navy: #173a67;
    --accent-orange: #f58634;
    --text-navy: #173a67;
  }
  html, body {
    margin: 0;
    padding: 0;
    width: 1200px;
    height: 900px;
    overflow: hidden;
    background: var(--page-bg);
  }
  .canvas {
    position: relative;
    width: 1200px;
    height: 900px;
  }
  .business-card {
    position: absolute;
    left: 128px;
    top: 180px;
    width: 944px;
    height: 538px;
    background: var(--card-navy);
    border-radius: 28px;
    overflow: hidden;
  }
  .website-band {
    position: absolute;
    left: 222px;
    top: 222px;
    right: 0;
    height: 94px;
    background: var(--accent-orange);
    border-radius: 20px 0 0 20px;
    display: flex;
    align-items: center;
  }
  .website-url {
    margin: 0 0 0 68px;
    font-family: "Source Sans 3", "Myriad Pro", sans-serif;
    font-weight: 400;
    font-size: 36px;
    letter-spacing: 0.2px;
    color: var(--text-navy);
  }
</style>
</head>
<body>
  <main class="canvas">
    <section class="business-card" aria-label="Business card back">
      <div class="website-band">
        <p class="website-url">www.brightlanesites.com</p>
      </div>
    </section>
  </main>
</body>
</html>
```